Powerpoint template for basic scientists studying immunology

We are an QFB-funded consortium of basic science researchers at academic centers in Boston, Philadelphia and Oxford, UK. We study why the immune system fails to get rid of Hepatitis C virus, and whether new antiviral treatments that reduce viral load improve immune function. We are looking for a powerpoint template that we can use as a "brand" for our research consortium. It would feature a logo (file attached) and should represent the fonts/colors contained in the logo. We we would present at meetings and to program officers at the QFB, but, if we ever get around to it, would also be on a website.

The scientific description is as follows:
Hepatitis C virus (HCV) infects 185 million persons worldwide, is the leading indication for liver transplantation and, in the US, has a higher mortaliy rate than HIV. The annual healthcare costs associated with HCV exceed $9 billion, a number expected to increase as the epidemic matures and end stage liver disease peaks over the next decade. By virtue of its remarkable predilection for persistence, HCV is a model chronic viral infection. Mounting evidence supports the idea that HCV, while inducing type I IFN expression, maintains chronicity by virtue of global suppression of host innate and adaptive immunity. The mainstay of treatment for the last two decades, IFN-α-based regimens are ineffective in many patient subgroups and have significant side effects. The recent development of highly effective direct acting antivirals (DAA) against HCV promises to alter the landscape of this devastating infection by offering curative therapy without IFN. However, it remains essential that we understand what type of immunity remains following pharmacological eradication of the virus because: a) many HCV infected subjects remain at risk for re-infection; and b) DAAs are only partially effective in some patient subgroups, particularly those with past treatment with IFN. The imminent availability of IFN-free treatment for HCV offers an unprecedented opportunity to understand broad questions about alterations in immunity in humans with cure of chronic infections. Until now, mechanistic dissection of human immune responses has been challenging due to limited ability to directly perturb the system. The organizing principle of this U19 Program therefore, is to capitalize on the unique opportunity to, for the first time, cure chronic viral infection in humans without immune modulation and interrogate the immunological changes that ensue. Thus, we have formulated the following central hypothesis for this Program: DAA-mediated cure of chronic HCV infection will lead to partial "resetting" of some immune abnormalities, but specific immunological defects will persist in some subjects that prevent development of optimal immunity to HCV. We will test this hypothesis through a set of integrated Projects and Cores.

Target Market(s)

scientists.

Industry/Entity Type

Biotechnology

Font styles to use
Sans Serif

Requirements
Must have
• Very clean, very simple. Mostly whitespace for puting graphs and data on. Colors, fonts should match the logo. Please see ppt example.
Should not have
• too much of the ppt covered with the logo.

```html
<!DOCTYPE html>
<html lang="en">
<head>
<meta charset="utf-8">
<title>HCV Consortium – Slide</title>
<link href="https://fonts.googleapis.com/css2?family=Arimo:wght@400;700&display=swap" rel="stylesheet">
<style>
  :root {
    --bg: #ffffff;
    --ink: #111111;
    --brand-blue: #0a9ddb;
    --brand-green: #6cb43f;
    --rule-dark: #1a1a1a;
  }
  * { margin: 0; padding: 0; box-sizing: border-box; }
  html, body {
    width: 1200px;
    height: 900px;
    overflow: hidden;
    background: var(--bg);
  }
  .slide {
    position: relative;
    width: 1200px;
    height: 900px;
    background: var(--bg);
    font-family: "Arimo", Arial, sans-serif;
    color: var(--ink);
  }
  .corner-mark {
    position: absolute;
    left: 0;
    top: 0;
    width: 158px;
    height: 136px;
    background: linear-gradient(135deg, var(--brand-green) 0%, var(--brand-blue) 70%);
    opacity: 0.85;
    clip-path: polygon(0 10%, 55% 0, 100% 0, 100% 45%, 75% 100%, 45% 100%, 0 75%);
  }
  .header-rule {
    position: absolute;
    left: 132px;
    top: 67px;
    width: 1008px;
    height: 3px;
    background: var(--brand-blue);
  }
  .content {
    position: absolute;
    left: 240px;
    top: 216px;
    height: 492px;
    border-left: 2px solid var(--rule-dark);
    padding-left: 57px;
  }
  .title {
    font-size: 48px;
    font-weight: 700;
    letter-spacing: 0.5px;
    line-height: 1;
    color: var(--brand-blue);
    margin-top: 14px;
    margin-bottom: 10px;
  }
  .title .abbr { color: var(--brand-green); }
  .fact {
    font-size: 29.5px;
    line-height: 39.6px;
    letter-spacing: 0.6px;
    white-space: nowrap;
  }
  .fact + .fact { margin-top: 39.6px; }
  .fact strong { font-weight: 700; }
</style>
</head>
<body>
  <main class="slide">
    <div class="corner-mark" role="img" aria-label="Cluster of blue and green hexagon ornaments"></div>
    <div class="header-rule"></div>

    <section class="content">
      <h1 class="title">Hepatitis C Virus <span class="abbr">(HCV)</span></h1>
      <p class="fact">
        <strong>infects 185 million persons</strong> worldwide,<br>
        is the leading indication for<br>
        liver transplantation and, in the US,<br>
        has a <strong>higher mortality rate than HIV.</strong>
      </p>
      <p class="fact">
        The <strong>annual healthcare</strong> costs associated<br>
        with HCV <strong>exceeds $9 billion</strong>,<br>
        a number expected to increase<br>
        as the epidemic matures and end stage<br>
        liver disease peaks over the next decade
      </p>
    </section>
  </main>
</body>
</html>
```